Short term accommodation - Guest feedback flyer

We provide short term fully self contained accommodation for couples,families and friends who require accommodation close to Brisbane City. We have 3 properties - http://www.restnook.com.au/accommodation/qld/brisbane/fernvale. Our properties are advertised on a on a number of online booking sites - such as roam critic, nest finder, restnook etc. Our accommodation is fully self contained, a nest finder from home! Our accommodation is affordable and located near or on transport routes so our guests can travel to all tourist attractions with ease. We provide a personal, professional and family friendly experience and we would like to capture our guests comments on their stay with the view to then posting their comments online so other guests can read about their experiences. Most guests don't have the time to leave their comments online once they check out. Id like a flyer to give to them before they check out so they have time to provide their feedback before they leave, I'll then take their feedback and upload it for them. A lot of travellers like to read online reviews before they book and I'd like the flyer to make it easy for guests to leave their feedback and I'll take it and post it for them. I hope by posting more comments on our webpages that our bookings will increase. Im happy for your to use any of the images/photos that are used on our restnook pages…….ive added the link about. Id like one generic flyer that I can use for all 3 properties please.

Thanks.

```html
<!DOCTYPE html>
<html lang="en">
<head>
<meta charset="utf-8">
<title>Guest Feedback Flyer – Fernvale</title>
<link href="https://fonts.googleapis.com/css2?family=Roboto+Condensed:wght@400;700&family=Roboto:wght@400;700&family=Comfortaa:wght@400&display=swap" rel="stylesheet">
<style>
  :root {
    --paper: #ebebed;
    --sky: #5ab4e0;
    --leaf: #3fae3f;
    --leaf-dark: #2e8f35;
    --ink: #2e3192;
    --note: #f4f4f4;
    --note-shade: #d2d2d2;
    --clip: #9a9ea3;
  }
  * { margin: 0; padding: 0; box-sizing: border-box; }
  html, body { width: 1200px; height: 881px; overflow: hidden; background: var(--paper); }
  .flyer { position: relative; width: 1200px; height: 881px; background: var(--paper); font-family: "Roboto", Arial, sans-serif; }
  .backdrop { position: absolute; inset: 0; }
  .headline {
    position: absolute; top: 34px; left: 0; width: 100%; text-align: center;
    font-family: "Roboto Condensed", "Arial Narrow", sans-serif; font-weight: 400;
    font-size: 36px; color: var(--ink); letter-spacing: 0.2px;
  }
  .suburb-badge {
    position: absolute; left: 60px; top: 108px; width: 370px; height: 96px;
    border-radius: 50%; background: var(--leaf);
    display: flex; align-items: center; justify-content: center;
    font-family: "Roboto Condensed", "Arial Narrow", sans-serif;
    font-size: 36px; color: #fff; letter-spacing: 0.5px;
  }
  .photos { position: absolute; left: 0; top: 0; width: 700px; height: 720px; }
  .feedback-note { position: absolute; left: 628px; top: 128px; width: 545px; height: 570px; filter: drop-shadow(4px 6px 6px rgba(0,0,0,0.25)); }
  .feedback-label {
    position: absolute; left: 773px; top: 201px; width: 250px; text-align: center;
    font-family: "Comfortaa", sans-serif; font-size: 30px; color: var(--leaf-dark);
  }
  .listings { position: absolute; top: 733px; left: 470px; display: flex; align-items: center; gap: 44px; }
  .listing { display: flex; align-items: center; gap: 10px; font-family: "Roboto", Arial, sans-serif; font-size: 30px; color: var(--ink); }
  .listing-mark { width: 32px; height: 32px; background: var(--leaf); }
  .listing-mark.round { border-radius: 50%; background: var(--ink); }
  .web-address {
    position: absolute; top: 800px; left: 60px; width: 1080px;
    display: flex; align-items: center; justify-content: center; gap: 12px;
    font-family: "Roboto", Arial, sans-serif; font-weight: 700; font-size: 30px; color: var(--ink);
  }
</style>
</head>
<body>
<main class="flyer">
  <svg class="backdrop" viewBox="0 0 1200 881" width="1200" height="881" aria-hidden="true">
    <path class="sky-band" fill="var(--sky)" d="M0 150 C 250 135, 500 190, 760 165 C 950 145, 1100 125, 1200 120 L1200 745 C 1000 735, 700 700, 400 700 C 250 700, 100 705, 0 712 Z"/>
    <path class="swoosh-top" fill="var(--leaf)" d="M720 160 C 900 120, 1080 100, 1200 92 L1200 125 C 1080 122, 900 135, 720 160 Z"/>
    <path class="swoosh-bottom" fill="var(--leaf)" d="M0 712 C 150 702, 330 705, 480 712 C 330 715, 150 728, 0 748 Z"/>
  </svg>

  <h1 class="headline">Accommodation close to Brisbane City for couples, families and friends</h1>
  <div class="suburb-badge">FERNVALE</div>

  <svg class="photos" viewBox="0 0 700 720" width="700" height="720">
    <defs>
      <linearGradient id="houseTone" x1="0" y1="0" x2="0" y2="1">
        <stop offset="0" stop-color="#3f6fb8"/><stop offset="0.55" stop-color="#d9d6c8"/><stop offset="1" stop-color="#6f8a4a"/>
      </linearGradient>
      <linearGradient id="bedroomTone" x1="0" y1="0" x2="1" y2="1">
        <stop offset="0" stop-color="#6a5646"/><stop offset="0.5" stop-color="#e3dcd2"/><stop offset="1" stop-color="#2a3a48"/>
      </linearGradient>
      <linearGradient id="loungeTone" x1="0" y1="0" x2="1" y2="1">
        <stop offset="0" stop-color="#e8d9bd"/><stop offset="0.6" stop-color="#b59a78"/><stop offset="1" stop-color="#2b2422"/>
      </linearGradient>
    </defs>
    <g role="img" aria-label="Photo of the raised timber Queenslander house with verandah">
      <ellipse cx="321" cy="355" rx="198" ry="131" fill="url(#houseTone)"/>
    </g>
    <g role="img" aria-label="Photo of the bedroom with queen bed and teal cushions">
      <ellipse cx="185" cy="580" rx="153" ry="114" fill="url(#bedroomTone)"/>
    </g>
    <g role="img" aria-label="Photo of the lounge room with leather sofas">
      <ellipse cx="456" cy="550" rx="165" ry="131" fill="url(#loungeTone)"/>
    </g>
  </svg>

  <svg class="feedback-note" viewBox="0 0 545 570" width="545" height="570" aria-hidden="true">
    <defs>
      <linearGradient id="noteFace" x1="0" y1="0" x2="1" y2="1">
        <stop offset="0" stop-color="#fbfbfb"/><stop offset="0.7" stop-color="var(--note)"/><stop offset="1" stop-color="var(--note-shade)"/>
      </linearGradient>
    </defs>
    <path fill="url(#noteFace)" d="M12 30 C 150 22, 330 26, 520 18 C 510 150, 525 330, 530 540 C 380 548, 200 552, 40 556 C 55 480, 40 430, 22 400 C 6 280, 18 150, 12 30 Z"/>
    <path fill="none" stroke="#cfcfcf" stroke-width="2" d="M40 556 C 55 480, 40 430, 22 400"/>
    <g class="paperclip" fill="none" stroke="var(--clip)" stroke-width="4" stroke-linecap="round">
      <path d="M110 70 L 120 10 C 122 0, 134 0, 132 12 L 124 60 C 123 66, 116 66, 117 58 L 124 20"/>
      <path d="M440 55 L 425 8 C 421 -2, 410 2, 413 12 L 428 52 C 430 58, 437 56, 435 50 L 424 22"/>
    </g>
  </svg>
  <p class="feedback-label">feedback</p>

  <div class="listings">
    <span class="listing"><span class="listing-mark"></span>restnook</span>
    <span class="listing"><span class="listing-mark round"></span>roam critic</span>
    <span class="listing">nest finder</span>
  </div>

  <p class="web-address">
    <svg width="26" height="26" viewBox="0 0 26 26" aria-hidden="true" fill="none" stroke="var(--ink)" stroke-width="2.2">
      <circle cx="13" cy="13" r="11"/><ellipse cx="13" cy="13" rx="5" ry="11"/><line x1="2" y1="13" x2="24" y2="13"/><line x1="4" y1="7" x2="22" y2="7"/><line x1="4" y1="19" x2="22" y2="19"/>
    </svg>
    www.restnook.com.au/accommodation/qld/brisbane/fernvale
  </p>
</main>
</body>
</html>
```